Business Card - Rebranding for Consulting Firm

We are renaming and rebranding our consulting firm and need to raise the level of quality of our cards as part of that effort. We consult to leading high tech, life science and other innovation sector companies.

Need a two-sided business card design.

Side 1: (a) Company logo (b) tag line: Build Lasting Value Through People (c) Name (d) Title (e) Phone 1: Office (f) Phone 2: Mobile (g) email: person@HollowmereAdvisory.com

Side 2: Two lines of text: (a) Vision Sets Direction. Agility Sustains Pace. People Deliver Results. (b) We help you master every one.

Target Market(s)

Business and human resources executives and senior managers

Industry/Entity Type

Management Consulting

Contact Information for Business Card

Font styles to use
Sans Serif

Requirements
Must have
• clean, not too busy, but with a bit of creativity. Stick to the colors used in the attached logo
• appeal to high tech, life science companies
Nice to have
• prefer white background

```html
<!DOCTYPE html>
<html lang="en">
<head>
<meta charset="utf-8">
<title>Hollowmere Advisory – Business Card</title>
<link href="https://fonts.googleapis.com/css2?family=Mulish:wght@300;400&family=Nunito:wght@800&display=swap" rel="stylesheet">
<style>
  :root {
    --bg: #e6cfc2;
    --card: #1c1c1c;
    --blue: #1f7fc0;
    --blue-deep: #176aa6;
    --text: #d2d2d2;
    --muted: #9a9a9a;
    --rule: #4a4a4a;
  }
  * { margin: 0; padding: 0; box-sizing: border-box; }
  html, body { width: 1200px; height: 779px; overflow: hidden; }
  body {
    background: var(--bg);
    font-family: "Mulish", sans-serif;
    font-weight: 300;
    color: var(--text);
    position: relative;
  }
  .card {
    position: absolute;
    top: 234px;
    width: 540px;
    height: 310px;
    background: var(--card);
  }
  .card--contact { left: 40px; }
  .card--message { left: 620px; }

  /* Contact side */
  .person { position: absolute; left: 38px; top: 44px; }
  .person__name {
    font-family: "Nunito", sans-serif;
    font-weight: 800;
    font-size: 21px;
    color: var(--blue);
    line-height: 1.1;
  }
  .person__title { font-size: 15px; color: var(--text); margin-top: 2px; }
  .brand-mini {
    position: absolute; right: 38px; top: 46px;
    display: flex; align-items: center; gap: 8px;
    font-size: 17px; font-weight: 400; color: var(--blue);
  }
  .brand-square { width: 14px; height: 14px; background: var(--blue-deep); flex: none; }
  .short-rule {
    position: absolute; left: 38px; top: 128px;
    width: 42px; height: 1px; background: var(--rule);
  }
  .address {
    position: absolute; left: 38px; top: 166px;
    font-size: 14.5px; line-height: 18.5px; font-style: normal;
  }
  .address__company { color: var(--blue); }
  .contacts {
    position: absolute; left: 254px; top: 166px;
    list-style: none; font-size: 14.5px; line-height: 18.5px;
  }
  .contacts li { display: flex; align-items: center; gap: 8px; }
  .contacts svg { width: 11px; height: 11px; fill: var(--blue); flex: none; }
  .tagline-row {
    position: absolute; left: 38px; right: 38px; top: 264px;
    display: flex; align-items: center; gap: 14px;
    font-size: 13.5px;
  }
  .tagline-row .line { flex: 1; height: 1px; background: var(--rule); }

  /* Message side */
  .brand-lockup {
    position: absolute; left: 0; right: 0; top: 90px;
    display: flex; justify-content: center; align-items: center; gap: 14px;
    font-size: 40px; font-weight: 400; color: var(--blue);
    letter-spacing: -0.5px;
  }
  .brand-lockup .brand-square { width: 26px; height: 26px; }
  .statement {
    position: absolute; right: 84px; top: 248px; width: 392px;
    font-size: 12.5px; color: var(--text);
  }
  .statement__first { text-align: right; }
  .statement__second {
    display: flex; align-items: center; gap: 12px; margin-top: 8px;
  }
  .statement__second .line { flex: 1; height: 1px; background: var(--rule); }
</style>
</head>
<body>

<section class="card card--contact">
  <div class="person">
    <p class="person__name">Daniel Reyes</p>
    <p class="person__title">Marketing Director</p>
  </div>
  <div class="brand-mini"><span class="brand-square"></span>Hollowmere</div>
  <div class="short-rule"></div>
  <address class="address">
    <p class="address__company">Hollowmere Advisory</p>
    <p>18 Alder Crest Road</p>
    <p>P.O. Box 2917</p>
    <p>Linwood, NJ 08221</p>
  </address>
  <ul class="contacts">
    <li><svg viewBox="0 0 12 12"><path d="M3 0h6v12H3z M4 1.5v8h4v-8z" fill-rule="evenodd"/></svg>000 000 0000</li>
    <li><svg viewBox="0 0 12 12"><path d="M2 1l2.5-.5 1.3 3-1.5 1a7 7 0 003.2 3.2l1-1.5 3 1.3L11 10c-5 .5-9.5-4-9-9z"/></svg>000 000 0000</li>
    <li><svg viewBox="0 0 12 12"><path d="M3 0h6v3H3zM1 4h10v5H9v3H3V9H1zM4 8v3h4V8z" fill-rule="evenodd"/></svg>person@HollowmereAdvisory.com</li>
    <li><svg viewBox="0 0 12 12"><path d="M0 2h12v8H0zM1 3l5 3.5L11 3z" fill-rule="evenodd"/></svg>www.hollowmereadvisory.com</li>
  </ul>
  <div class="tagline-row"><span>Build Lasting Value Through People</span><span class="line"></span></div>
</section>

<section class="card card--message">
  <div class="brand-lockup"><span class="brand-square"></span>Hollowmere Advisory</div>
  <div class="statement">
    <p class="statement__first">Vision Sets Direction. Agility Sustains Pace. People Deliver Results.</p>
    <p class="statement__second"><span class="line"></span><span>We help you master every one.</span></p>
  </div>
</section>

</body>
</html>
```